Flyer Vacation Gift Certificate

I need to create a beautiful flyer 8.5 x 11 PDF format flyer design. <br/><br/>Instructions:<br/>The flyer will really be a gift voucher for a las vegas vacation getaway. So must have a Las Vegas Theme exciting fun<br/><br/>The voucher should have two modules that will be editable. <br/>Must have a "Compliments Of" area and also must have an "Exclusively For" area<br/><br/>Keep in mind that this flyer will be printed so keep that in mind :)<br/><br/>Here the is the content for the vacation voucher:<br/><br/>There is no doubt that Las Vegas is one of the hottest travel destinations around the world. In fact, some people would even go as far as<br/>saying that perhaps it is THE hottest place to visit. Enjoy up to 4 nights of resort/casino accommodations in exciting Las Vegas, NV. Millions of people travel to this exciting city each year to enjoy its thrills. Thanks to the business you received this certificate from, now you can enjoy exciting Las Vegas, NV too!<br/><br/>Features:<br/>*Travel 7 Days A Week<br/>*Stay Your Choice Of Nights (1-4 Nights)<br/>*Good For Two Adults & Two Children<br/>*Pay Just The Taxes & Fees<br/>*Multiple Travel Date Requests Allowed<br/>*Fully Transferable To Another Person<br/>*Just A 30 Days Advance Notice Required<br/>*You Will Have 12 Months To Complete Travel After Redemption<br/><br/>HOW CAN WE DO THIS?<br/><br/>We contract with the world leading hotel chains and resorts to help them fill their otherwise empty rooms.<br/><br/>We help fill empty rooms which the hotels, resorts and cruise lines turn into additional revenue from other areas of their property and future bookings.<br/><br/>Hotels rarely experience full occupancy, yet they remain open, providing rooms and services at fixed costs. So when hotels give out their rooms by partnering with marketing companies like us, they might miss out on the room fee, but they already didn't have that in the first place, at least now they have the opportunity to gain a customer for their in-house restaurants, room service, their casinos, an extra day stay, future bookings, etc.<br/><br/>VIEW ALL THE DETAILS OF THIS SPECIAL OFFER AND REDEEM ONLINE AT <br/>WWW.TOPAZVOUCHERDESK.COM<br/><br/>Certificate ID # 47261-38504<br/>Expires 02/29/2020<br/><br/><br/>*terms and conditions apply see website for details<br/><br/>KEEP IN MIND THE EXAMPLES I AM UPLOADING ARE SIMPLY TO SHOW YOU THAT THEY CONTAIN THE "COMPLIMENTS OF" AND "EXCLUSIVELY FOR" ELEMENTS. THESE MUST BE INCLUDED IN NEW DESIGN. PLEASE ONLY USE THE CONTENT I PROVIDED IN BRIEF, DONT USE CONTENT FROM EXAMPLES.

Target Market(s)

CONSUMERS THAT HAVE BEEN REWARDED WITH A VACATION CERTIFICATE FOR DOING BUSINESS WITH A COMPANY.

COMPANIES USE THESE AS MARKETING INCENTIVES TO ATTRACT MORE CUSTOMERS AND TO REWARD LOYALTY, ETC.

Industry/Entity Type

Travel Industry

Colors

Designer to choose colors to be used in the design.

Requirements
Must have
• I need to create a beautiful flyer 8.5 x 11 PDF format flyer design.
• Instructions:
• The flyer will really be a gift voucher for a las vegas vacation getaway. So must have a Las Vegas Theme exciting fun
• The voucher should have two modules that will be editable.
• Must have a "Compliments Of" area and also must have an "Exclusively For" area
• Keep in mind that this flyer will be printed so keep that in mind :)
• Here the is the content for the vacation voucher:
• There is no doubt that Las Vegas is one of the hottest travel destinations around the world. In fact, some people would even go as far as
• saying that perhaps it is THE hottest place to visit. Enjoy up to 4 nights of resort/casino accommodations in exciting Las Vegas, NV. Millions of people travel to this exciting city each year to enjoy its thrills. Thanks to the business you received this certificate from, now you can enjoy exciting Las Vegas, NV too!
• Features:
• *Travel 7 Days A Week
• *Stay Your Choice Of Nights (1-4 Nights)
• *Good For Two Adults & Two Children
• *Pay Just The Taxes & Fees
• *Multiple Travel Date Requests Allowed
• *Fully Transferable To Another Person
• *Just A 30 Days Advance Notice Required
• *You Will Have 12 Months To Complete Travel After Redemption
• HOW CAN WE DO THIS?
• We contract with the world leading hotel chains and resorts to help them fill their otherwise empty rooms.
• We help fill empty rooms which the hotels, resorts and cruise lines turn into additional revenue from other areas of their property and future bookings.
• Hotels rarely experience full occupancy, yet they remain open, providing rooms and services at fixed costs. So when hotels give out their rooms by partnering with marketing companies like us, they might miss out on the room fee, but they already didn't have that in the first place, at least now they have the opportunity to gain a customer for their in-house restaurants, room service, their casinos, an extra day stay, future bookings, etc.
• VIEW ALL THE DETAILS OF THIS SPECIAL OFFER AND REDEEM ONLINE AT
• WWW.TOPAZVOUCHERDESK.COM
• Certificate ID # 47261-38504
• Expires 02/29/2020
• *terms and conditions apply see website for details
• KEEP IN MIND THE EXAMPLES I AM UPLOADING ARE SIMPLY TO SHOW YOU THAT THEY CONTAIN THE "COMPLIMENTS OF" AND "EXCLUSIVELY FOR" ELEMENTS. THESE MUST BE INCLUDED IN NEW DESIGN. PLEASE ONLY USE THE CONTENT I PROVIDED IN BRIEF, DONT USE CONTENT FROM EXAMPLES.
Nice to have
• EXCITING LAS VEGAS IMAGES THAT MAKE SOMEONE WANT TO GO THERE

```html
<!DOCTYPE html>
<html lang="en">
<head>
<meta charset="utf-8">
<title>Vacation Gift Las Vegas</title>
<link href="https://fonts.googleapis.com/css2?family=Arimo:wght@400;700&display=swap" rel="stylesheet">
<style>
  :root {
    --navy: #2b2f8c;
    --navy-deep: #1e2470;
    --royal: #2e4a9e;
    --gold: #f7c21c;
    --gold-soft: #fde7a6;
    --orange: #fbb23a;
    --sky-top: #2fb4ea;
    --sky-mid: #4a7fd0;
    --water: #1f3fa8;
    --ink: #111111;
    --white: #ffffff;
  }
  * { margin: 0; padding: 0; box-sizing: border-box; }
  html, body { width: 927px; height: 1200px; overflow: hidden; background: var(--white); }
  body { font-family: "Arimo", Arial, sans-serif; color: var(--ink); }
  .voucher { position: relative; width: 927px; height: 1200px; overflow: hidden; }
  .voucher__art { position: absolute; inset: 0; }

  .compliments {
    position: absolute; left: 10px; top: 16px;
    color: var(--gold); font-weight: 700; font-size: 23px; line-height: 36px;
    text-align: center; width: 255px;
  }
  .title { position: absolute; right: 36px; top: 24px; text-align: center; color: var(--white); font-weight: 700; }
  .title__kicker { font-size: 38px; letter-spacing: 1px; line-height: 44px; }
  .title__city { font-size: 66px; letter-spacing: 1px; line-height: 74px; }

  .exclusive {
    position: absolute; left: 0; top: 391px; width: 272px; height: 84px;
    border-radius: 0 42px 42px 0;
    background: linear-gradient(90deg, var(--gold-soft), var(--orange));
    padding: 14px 0 0 21px;
    color: var(--navy-deep); font-weight: 700; font-size: 22px; line-height: 27px;
  }

  .section-title { position: absolute; left: 0; width: 927px; text-align: center; color: var(--royal); font-weight: 700; }
  .section-title--intro { top: 508px; font-size: 27px; }
  .section-title--features { top: 657px; font-size: 27px; }
  .section-title--how { top: 820px; font-size: 27px; }

  .copy { position: absolute; left: 60px; width: 807px; text-align: center; font-size: 15.4px; line-height: 20px; }
  .copy--intro { top: 548px; padding: 0 40px; }
  .copy--how { top: 858px; }

  .features { position: absolute; top: 700px; list-style: none; font-size: 17px; line-height: 21.7px; }
  .features--left { left: 56px; }
  .features--right { left: 540px; width: 360px; }
  .features li { position: relative; padding-left: 19px; }
  .features li::before {
    content: ""; position: absolute; left: 0; top: 5px;
    width: 11px; height: 11px; border-radius: 50%; background: var(--royal);
  }

  .certificate { position: absolute; top: 998px; left: 0; width: 927px; text-align: center; font-size: 15.4px; line-height: 20px; }

  .footer { position: absolute; left: 0; top: 1114px; width: 927px; text-align: center; color: var(--gold); font-weight: 700; }
  .footer__cta { font-size: 16px; line-height: 28px; }
  .footer__url { font-size: 16px; line-height: 26px; }
  .footer__terms { font-size: 15px; line-height: 26px; }
</style>
</head>
<body>
<main class="voucher">
  <svg class="voucher__art" width="927" height="1200" viewBox="0 0 927 1200" aria-hidden="false">
    <defs>
      <linearGradient id="skyline" x1="0" y1="0" x2="0" y2="1">
        <stop offset="0" stop-color="var(--sky-top)"/>
        <stop offset="0.35" stop-color="var(--sky-mid)"/>
        <stop offset="0.62" stop-color="#c9a27a"/>
        <stop offset="0.7" stop-color="#3c6fd0"/>
        <stop offset="1" stop-color="var(--navy-deep)"/>
      </linearGradient>
      <linearGradient id="goldband" x1="0" y1="0" x2="1" y2="0">
        <stop offset="0" stop-color="var(--gold-soft)"/>
        <stop offset="0.5" stop-color="var(--gold)"/>
        <stop offset="1" stop-color="var(--orange)"/>
      </linearGradient>
      <linearGradient id="footerfill" x1="0" y1="0" x2="1" y2="0">
        <stop offset="0" stop-color="var(--navy)"/>
        <stop offset="0.8" stop-color="var(--navy)"/>
        <stop offset="1" stop-color="#5650a2"/>
      </linearGradient>
    </defs>

    <path class="hero-rim" d="M0 338 C200 330 300 430 380 468 C440 496 510 492 570 452 C650 400 780 332 927 330 V362 C790 360 660 420 580 468 C520 502 440 506 375 478 C290 440 200 355 0 362 Z" fill="url(#goldband)"/>
    <path class="hero-photo" role="img" aria-label="Las Vegas resort and casino skyline at dusk reflected on the water"
      d="M0 0 H927 V340 C780 345 650 405 575 452 C510 492 440 494 380 466 C300 430 200 335 0 345 Z" fill="url(#skyline)"/>

    <path class="corner-rim" d="M0 100 C60 130 140 150 210 135 C290 115 340 40 410 0 H430 C360 50 300 135 215 145 C140 152 60 135 0 115 Z" fill="var(--gold)"/>
    <path class="corner-badge" d="M0 0 H410 C340 40 290 115 210 130 C140 142 60 122 0 95 Z" fill="var(--navy)"/>

    <path class="footer-rim" d="M0 1000 C140 985 300 1000 420 1060 C480 1090 540 1094 600 1070 C720 1020 820 995 927 1000 V1030 C830 1010 720 1040 600 1090 C540 1112 480 1110 420 1080 C300 1025 150 1012 0 1040 Z" fill="url(#goldband)"/>
    <path class="footer-band" d="M0 1040 C150 1012 300 1025 420 1080 C480 1110 540 1112 600 1090 C720 1040 830 1010 927 1030 V1200 H0 Z" fill="url(#footerfill)"/>
  </svg>

  <div class="compliments">THIS CERTIFICATE IS<br>COMPLIMENTS OF</div>

  <header class="title">
    <div class="title__kicker">VACATION GIFT</div>
    <div class="title__city">LAS VEGAS</div>
  </header>

  <div class="exclusive">EXCLUSIVELY FOR:<br>CUSTOMER NAME</div>

  <h2 class="section-title section-title--intro">THE CONTENT FOR THE VACATION VOUCHER</h2>
  <p class="copy copy--intro">There is no doubt that Las Vegas is one of the hottest travel destinations around the world. In fact, some people would even go as far as saying that perhaps it is THE hottest place to visit. Enjoy up to 4 nights of resort/casino accommodations in exciting Las Vegas, NV. Millions of people travel to this exciting city each year to enjoy its thrills. Thanks to the business you received this certificate from, now you can enjoy exciting Las Vegas, NV too!</p>

  <h2 class="section-title section-title--features">FEATURES</h2>
  <ul class="features features--left">
    <li>Travel 7 Days A Week</li>
    <li>Good For Two Adults &amp; Two Children</li>
    <li>Multiple Travel Date Requests Allowed</li>
    <li>Just A 30 Days Advance Notice Required</li>
  </ul>
  <ul class="features features--right">
    <li>Stay Your Choice Of Nights (1-4 Nights)</li>
    <li>Pay Just The Taxes &amp; Fees</li>
    <li>Fully Transferable To Another Person</li>
    <li>You Will Have 12 Months To Complete Travel After Redemption</li>
  </ul>

  <h2 class="section-title section-title--how">HOW CAN WE DO THIS?</h2>
  <p class="copy copy--how">We contract with the world leading hotel chains and resorts to help them fill their otherwise empty rooms. We help fill empty rooms which the hotels, resorts and cruise lines turn into additional revenue from other areas of their property and future bookings. Hotels rarely experience full occupancy, yet they remain open, providing rooms and services at fixed costs. So when hotels give out their rooms by partnering with marketing companies like us, they might miss out on the room fee, but they already didn’t have that in the first place, at least now they have the opportunity to gain a customer for their in-house restaurants, room service, their casinos, an extra day stay, future bookings, etc.</p>

  <div class="certificate">
    <div>Certificate ID # 47261-38504,</div>
    <div>Expires 02 / 29 / 2020</div>
  </div>

  <footer class="footer">
    <div class="footer__cta">VIEW ALL THE DETAILS OF THIS SPECIAL OFFER AND REDEEM ONLINE AT</div>
    <div class="footer__url">WWW.TOPAZVOUCHERDESK.COM</div>
    <div class="footer__terms">terms and conditions apply see website for details</div>
  </footer>
</main>
</body>
</html>
```